Brand Business Card for Hotel Cloud Management System

Hello designers,
we are looking for a new brand business card for our product Roomvanta. Our brand Roomvanta is a hotel management system for small hotels, B&B, guesthouses etc. and just recently we are expanding our offer to other European markets. Therefore we need a business card that will communicate not only to the end-users (hoteliers) but also to potential business partners/ We would like the brand business card to be professional looking, but not too serius, modern, elegant, clean, Our brand color is orange, dark grey and it would be nice to see both combined.

Please visit our website www.roomvanta-example.eu to get more impression on what our brand roomvanta stands for.

Please find attached roomvanta logo.

Target Market(s)

small hotels, hoteliers, B&B owners, potential business partners

Industry/Entity Type

Software Service

Contact Information for Business Card

Roomvanta
- hotel software solutions - web booking engine - multi channel manager
www.roomvanta-example.eu
T: +38614007300
E: info@roomvanta-example.net

Font styles to use
Serif
Sans Serif

Colors
f37122
aaaaaa
606060
f6f6f6

Requirements
Must have
• Logo of the brand
• the layout of the business card should be in connection with the look and feel of the website roomvanta-example.eu and logo roomvanta;

```html
<!DOCTYPE html>
<html lang="en">
<head>
<meta charset="utf-8">
<title>Roomvanta Business Card</title>
<link href="https://fonts.googleapis.com/css2?family=Nunito:wght@400;800&family=Montserrat:wght@500;700&display=swap" rel="stylesheet">
<style>
  :root {
    --brand-orange: #e0600f;
    --ink: #1e1e1e;
    --dark-grey: #606060;
    --line-grey: #2b2b2b;
    --paper: #f6f6f6;
    --backdrop: #e6e6e8;
    --white: #ffffff;
  }
  html, body {
    margin: 0;
    width: 1200px;
    height: 1200px;
    overflow: hidden;
    background: var(--backdrop);
  }
  .card {
    position: absolute;
    left: 50px;
    top: 300px;
    width: 1100px;
    height: 600px;
    background: var(--paper);
    box-shadow: 0 10px 30px rgba(0,0,0,0.15);
    overflow: hidden;
    font-family: "Montserrat", sans-serif;
  }
  .card-shapes { position: absolute; inset: 0; }
  .brand {
    position: absolute;
    left: 405px;
    top: 176px;
    display: flex;
    align-items: flex-end;
    gap: 14px;
  }
  .brand-name {
    font-family: "Nunito", sans-serif;
    font-weight: 800;
    font-size: 104px;
    line-height: 1;
    color: var(--ink);
    letter-spacing: -2px;
  }
  .brand-square {
    width: 28px;
    height: 28px;
    background: var(--brand-orange);
    margin-bottom: 20px;
  }
  .brand-tagline {
    position: absolute;
    left: 410px;
    top: 266px;
    font-family: "Nunito", sans-serif;
    font-weight: 400;
    font-size: 44px;
    color: var(--ink);
  }
  .person {
    position: absolute;
    left: 63px;
    top: 372px;
  }
  .person-name {
    font-weight: 700;
    font-size: 35px;
    color: var(--white);
    line-height: 1.1;
  }
  .person-role {
    font-weight: 700;
    font-size: 25px;
    color: #4a4a4a;
  }
  .contacts {
    position: absolute;
    left: 63px;
    top: 472px;
    list-style: none;
    margin: 0;
    padding: 0;
  }
  .contacts li {
    display: flex;
    align-items: center;
    gap: 12px;
    height: 29px;
    font-weight: 500;
    font-size: 20px;
    letter-spacing: 1px;
    color: var(--white);
  }
  .contacts svg { width: 20px; height: 20px; }
  .services {
    position: absolute;
    left: 0;
    right: 0;
    bottom: 0;
    height: 36px;
    display: flex;
    justify-content: flex-end;
    align-items: center;
    gap: 36px;
    padding-right: 70px;
    font-weight: 500;
    font-size: 20px;
    letter-spacing: 1px;
    color: var(--white);
  }
  .services .dot {
    width: 8px; height: 8px; border-radius: 50%; background: var(--white);
  }
</style>
</head>
<body>
  <div class="card">
    <svg class="card-shapes" viewBox="0 0 1100 600" aria-hidden="true">
      <path d="M0,200 C250,200 450,455 680,450 C860,446 960,378 1100,356" fill="none" stroke="var(--line-grey)" stroke-width="10"/>
      <path d="M0,209 C250,209 450,464 680,459 C860,455 960,387 1100,365" fill="none" stroke="var(--dark-grey)" stroke-width="10"/>
      <path d="M0,214 C250,214 450,469 680,464 C860,460 960,392 1100,370 L1100,600 L0,600 Z" fill="var(--brand-orange)"/>
      <rect x="0" y="564" width="1100" height="36" fill="var(--dark-grey)"/>
    </svg>

    <div class="brand">
      <span class="brand-name">Roomvanta</span>
      <span class="brand-square"></span>
    </div>
    <div class="brand-tagline">hotel pms service</div>

    <div class="person">
      <div class="person-name">Marko Vidmar</div>
      <div class="person-role">Manager</div>
    </div>

    <ul class="contacts">
      <li>
        <svg viewBox="0 0 24 24"><path d="M6.6 3.5l3 3-1.8 2.4a13 13 0 0 0 7.3 7.3l2.4-1.8 3 3-2 2.6C11 19.5 4.5 13 4 5.5z" fill="var(--white)"/></svg>
        +38614007300
      </li>
      <li>
        <svg viewBox="0 0 24 24"><rect x="2" y="5" width="20" height="14" fill="none" stroke="var(--white)" stroke-width="2"/><path d="M2 6l10 7 10-7" fill="none" stroke="var(--white)" stroke-width="2"/></svg>
        info@roomvanta-example.net
      </li>
      <li>
        <svg viewBox="0 0 24 24"><circle cx="12" cy="12" r="9.5" fill="none" stroke="var(--white)" stroke-width="2"/><path d="M2.5 12h19M12 2.5c3 3 3 16 0 19M12 2.5c-3 3-3 16 0 19" fill="none" stroke="var(--white)" stroke-width="1.6"/></svg>
        www.roomvanta-example.eu
      </li>
    </ul>

    <div class="services">
      <span>Hotel Software Solutions</span>
      <span class="dot"></span>
      <span>Web Booking Engine</span>
      <span class="dot"></span>
      <span>Multi Channel Manager</span>
    </div>
  </div>
</body>
</html>
```